Seven Lanterns at Dusk.

I need a book cover (and back cover) design for a novel. The novel is a thiller. ´Synopsis: During the party after an awards ceremony at prestigious institution, one of the young awarders dissapear. The last place where he left a trace was close to a giant chessboard in the grass of the beautiful gardens of the place of ceremony. The detective in charge of finding the missing person and find out what happened will gradually discover that the institution is not all that it seems.
The book cover size will be 9" x 6" and the title of the novel "Seven lanterns at dusk" will be name in spanish "Siete faroles al anochecer". The back cover will have a synopsis (in spanish )that i will develop later on.
One suggestion for the design: I always love the art of OTTO PEMBERLY for movie posters, so I´m looking for something of similar style, you know (a widow beside copper rails, Harbor lamp waltz, mirrowen, ledger of silence, etc

```html
<!DOCTYPE html>
<html lang="es">
<head>
<meta charset="utf-8">
<title>Siete faroles al anochecer — contracubierta</title>
<link rel="stylesheet" href="https://fonts.googleapis.com/css2?family=Righteous&family=Source+Serif+4:opsz,wght@8..60,400&display=swap">
<style>
  :root {
    --green-top: #1a4220;
    --green-bottom: #285c34;
    --cream: #efe7db;
    --ink: #141a14;
    --rook: #111a13;
  }
  * { margin: 0; padding: 0; box-sizing: border-box; }
  html, body { width: 800px; height: 1200px; overflow: hidden; }
  body { background: var(--green-bottom); }
  .back-cover {
    position: relative;
    width: 800px;
    height: 1200px;
    overflow: hidden;
    background: linear-gradient(180deg, var(--green-top) 0%, var(--green-bottom) 100%);
  }
  .title {
    position: absolute;
    left: 106px;
    top: 168px;
    width: 600px;
    font-family: "Righteous", sans-serif;
    font-weight: 400;
    font-size: 36px;
    line-height: 1;
    letter-spacing: 0.5px;
    color: var(--cream);
    text-transform: uppercase;
    white-space: nowrap;
  }
  .tagline {
    position: absolute;
    left: 106px;
    top: 260px;
    width: 590px;
    font-family: "Righteous", sans-serif;
    font-size: 17.5px;
    line-height: 24px;
    color: var(--ink);
    text-transform: uppercase;
    opacity: 0.85;
  }
  .paper {
    position: absolute;
    left: 0;
    top: 0;
    width: 800px;
    height: 1200px;
  }
  .paper polygon { fill: var(--cream); }
  .synopsis {
    position: absolute;
    font-family: "Source Serif 4", serif;
    font-size: 17px;
    line-height: 22.2px;
    color: var(--ink);
  }
  .synopsis p + p { margin-top: 22px; }
  .synopsis--main { left: 127px; top: 379px; width: 545px; }
  .synopsis--beside { left: 319px; top: 739px; width: 360px; }
  .rook-silhouette {
    position: absolute;
    left: 0;
    top: 753px;
    width: 299px;
    height: 447px;
    background: var(--rook);
  }
</style>
</head>
<body>
  <main class="back-cover">
    <h1 class="title">Siete faroles al anochecer</h1>
    <p class="tagline">Lorem ipsum dolor sit amet, consectetuer adipiscing elit, sed diam nonummy nibh euismod tincidunt ut</p>

    <svg class="paper" viewBox="0 0 800 1200" aria-hidden="true">
      <polygon points="108,364 685,363 695,995 230,1003 103,727"/>
    </svg>

    <div class="synopsis synopsis--main">
      <p>Lorem ipsum dolor sit amet, consectetuer adipiscing elit, sed diam nonummy nibh euismod tincidunt ut laoreet dolore magna aliquam erat volutpat. Ut wisi enim ad minim veniam, quis nostrud exerci tation ullamcorper suscipit lobortis nisl ut aliquip ex ea commodo consequat. Duis autem vel eum iriure dolor in hendrerit in vulputate velit esse molestie consequat, vel illum dolore eu feugiat nulla facilisis at vero eros et accumsan et iusto odio dignissim qui blandit praesent luptatum zzril delenit augue duis dolore te feugait nulla facilisi.</p>
      <p>Lorem ipsum dolor sit amet, cons ectetuer adipiscing elit, sed diam nonummy nibh euismod tincidunt ut laoreet dolore magna aliquam erat volutpat. Ut wisi enim ad minim veniam, quis nostrud exerci tation ullamcorper suscipit lobortis nisl ut aliquip ex ea commodo consequat.</p>
    </div>

    <div class="synopsis synopsis--beside">
      <p>Lorem ipsum dolor sit amet, consectetuer adipiscing elit, sed diam nonummy nibh euismod tincidunt ut laoreet dolore magna aliquam erat volutpat. Ut wisi enim ad minim veniam, quis nostrud exerci tation ullamcorper suscipit lobortis nisl ut aliquip ex ea commodo consequat. Duis autem vel eum iriure dolor in hendrerit in vulputate velit esse molestie consequat, vel illum dolore eu feugiat nulla facilisis at vero eros et accumsan et iusto odio</p>
    </div>

    <div class="rook-silhouette" role="img" aria-label="Silueta oscura de una torre de ajedrez"></div>
  </main>
</body>
</html>
```